tarnu

We are a group of companies that we want to make a triptych. we want the general information of the work we do and the information of each company with its logo

```html
<!DOCTYPE html>
<html lang="es">
<head>
<meta charset="utf-8">
<title>Power Team Nexo Tarnu – Tríptico</title>
<link rel="stylesheet" href="https://fonts.googleapis.com/css2?family=Open+Sans:ital,wght@0,400;0,600;0,700;1,700&family=Archivo+Black&family=Arimo:wght@700&display=swap">
<style>
:root{
  --kraft:#b3885a;
  --sky:#7cc6dc;
  --amber:#f1b24c;
  --teal:#0f5877;
  --teal-dark:#0b4a66;
  --gold:#f7b718;
  --ink:#1d1d1b;
  --white:#ffffff;
  --paper:#f2f2f2;
  --label:#f3ece2;
}
*{margin:0;padding:0;box-sizing:border-box}
html,body{width:739px;height:1200px;overflow:hidden;background:var(--kraft)}
body{position:relative;font-family:"Open Sans",Arial,sans-serif;color:var(--ink)}
.side-label{position:absolute;width:226px;text-align:center;font-family:"Arimo",Arial,sans-serif;font-weight:700;font-size:13px;color:var(--label)}
.sheet{position:absolute;left:36px;width:672px;display:flex;box-shadow:2px 3px 6px rgba(0,0,0,.35)}
.sheet-outer{top:46px;height:524px}
.sheet-inner{top:606px;height:522px}
.panel{position:relative;height:100%;overflow:hidden}
.panel+.panel{border-left:1px dashed rgba(255,255,255,.45)}
.w1{width:226px}.w2{width:220px}
.bg-sky{background:var(--sky)}
.services{list-style:none;padding:0 10px 0 22px}
.services li{position:relative;font-size:6.9px;line-height:1.38;margin-bottom:2.4px;color:var(--ink)}
.services li::before{content:"";position:absolute;left:-13px;top:2.6px;width:4.6px;height:4.6px;background:var(--white)}
.services li.muted{color:#3d5560}
.heading{background:var(--amber);color:var(--white);font-weight:700;font-size:11px;line-height:1.28;padding:6px 12px 5px 20px;text-transform:uppercase;margin:8px 0 6px}
/* company panel */
.company-head{background:var(--amber);height:32px;margin-top:2px;display:flex;align-items:center;padding-left:18px;color:var(--white);font-style:italic;font-weight:700;font-size:14.5px}
.company-list{list-style:none;padding-top:10px}
.company{display:flex;align-items:center;height:58px;background:var(--paper);margin-bottom:10.5px;padding-left:12px}
.mark{width:100px;height:34px;display:flex;align-items:center;justify-content:center;gap:4px;font-weight:700;font-size:10.5px;background:var(--white);color:#333}
.mark.dark{background:#111;color:var(--white)}
.mark .dot{width:7px;height:7px;background:#e0532b}
.contact{margin-left:7px;font-size:7.6px;line-height:1.45}
.contact strong{font-weight:700}
.contact .phone{display:flex;align-items:center;gap:3px}
.company-foot{position:absolute;left:0;right:0;bottom:0;height:17px;background:var(--amber)}
/* cover */
.cover{background:var(--teal)}
.cover-title{margin-top:34px;text-align:center;font-family:"Archivo Black",Arial,sans-serif;font-size:34px;line-height:1.1;color:var(--gold);text-shadow:1px 2px 2px rgba(0,0,0,.35)}
.cover-sub{margin-top:30px;text-align:center;color:var(--white);font-size:14.5px;line-height:1.4}
.cover-band{position:absolute;left:0;right:0;top:278px;height:35px;background:#050505;color:var(--white);font-size:15px;display:flex;align-items:center;padding-left:31px}
.cover-photo{position:absolute;left:0;right:0;top:313px;height:146px;background:linear-gradient(135deg,#4d5358 0%,#b9bcbd 45%,#e6e7e6 60%,#7d7468 100%)}
.cover-web{position:absolute;left:0;right:0;top:462px;height:44px;background:#050505;color:var(--amber);font-weight:700;font-size:13.5px;letter-spacing:2.2px;display:flex;align-items:center;padding-left:28px}
.inner-strip{position:absolute;left:0;right:0;bottom:17px;height:7px;background:#e9f4f8}
</style>
</head>
<body>
<div class="side-label" style="left:36px;top:22px">Side 5</div>
<div class="side-label" style="left:262px;top:22px">Side 6</div>
<div class="side-label" style="left:482px;top:22px">Side 1</div>

<section class="sheet sheet-outer">
  <div class="panel w1 bg-sky">
    <ul class="services" style="padding-top:20px">
      <li>Instalación y mantenimiento de electricidad y domótica</li>
      <li>Instalación y mantenimiento de sistemas de alumbrado, tanto en interiores como en exteriores</li>
      <li>Instalación y mantenimiento de alumbrado de emergencia</li>
      <li>Instalación y mantenimiento de instalación de fontanería y saneamiento</li>
      <li>Instalación de ascensores</li>
      <li>Instalación y mantenimiento de instalaciones de protección especializada contra incendios mediante agua, gases inertes, sistemas especiales para cocinas industriales, columna seca, de-pósitos de agua, señalización, puertas cortafuegos, telas ignífugas o sellado de pasos de insta-laciones</li>
    </ul>
    <h2 class="heading" style="margin-top:12px">Diseño y gestión de proyectos y obras para empresas y negocios</h2>
    <ul class="services" style="padding-left:25px">
      <li>Proyecto de obra nueva</li>
      <li>Proyecto de reforma y rehabilitación</li>
      <li>Proyecto de interiorismo y decoración de hoteles, locales comerciales, oficinas y edificios públicos en general</li>
      <li>Estudio de viabilidad de promociones inmobiliarias</li>
      <li>Búsqueda de terrenos y edificios para promociones inmobiliarias, gestión patrimonial y grupos inversores</li>
      <li>Búsqueda de compradores e inversores para los inmuebles de nuestros clientes</li>
      <li>Proyecto de cambio de uso de edificios construidos, ya sean hoteles, viviendas, locales, ofici-nas, al uso que el cliente solicite, previa consulta con las administraciones competentes para validar la viabilidad del proceso</li>
      <li>Dirección de obra</li>
      <li>Proyecto de urbanización de terrenos ubicados en zonas afectadas por planes parciales</li>
      <li>Tramitación de licencia de obras ante ayuntamientos y administraciones equivalentes</li>
      <li>Comercialización y valoración de inmuebles, tanto para clientes nacionales como extranjeros que busquen propiedades en España</li>
    </ul>
  </div>

  <div class="panel w2" style="background:var(--white)">
    <h2 class="company-head">Información de la compañía</h2>
    <ul class="company-list">
      <li class="company"><span class="mark" style="background:#5a6470;color:#fff">Lumen Estudio</span><div class="contact"><strong>El nombre,</strong><div class="phone"><svg width="8" height="7" viewBox="0 0 8 7"><path d="M1 2.5C1 1 2 .5 4 .5S7 1 7 2.5H5.6V1.8H2.4v.7zM1.6 3h4.8L7 6.5H1z" fill="#1d1d1b"/></svg>012.345.6789</div>Elnombre@website.com<br><strong>www.website.com</strong></div></li>
      <li class="company"><span class="mark" style="color:#8cbf3f"><span class="dot" style="background:#8cbf3f"></span>Kaltra</span><div class="contact"><strong>El nombre,</strong><div class="phone"><svg width="8" height="7" viewBox="0 0 8 7"><path d="M1 2.5C1 1 2 .5 4 .5S7 1 7 2.5H5.6V1.8H2.4v.7zM1.6 3h4.8L7 6.5H1z" fill="#1d1d1b"/></svg>012.345.6789</div>Elnombre@website.com<br><strong>www.website.com</strong></div></li>
      <li class="company"><span class="mark" style="font-size:8.5px">Carpinterías Bravo</span><div class="contact"><strong>El nombre,</strong><div class="phone"><svg width="8" height="7" viewBox="0 0 8 7"><path d="M1 2.5C1 1 2 .5 4 .5S7 1 7 2.5H5.6V1.8H2.4v.7zM1.6 3h4.8L7 6.5H1z" fill="#1d1d1b"/></svg>012.345.6789</div>Elnombre@website.com<br><strong>www.website.com</strong></div></li>
      <li class="company"><span class="mark" style="color:#7a1f24;font-size:13px">Oreta</span><div class="contact"><strong>El nombre,</strong><div class="phone"><svg width="8" height="7" viewBox="0 0 8 7"><path d="M1 2.5C1 1 2 .5 4 .5S7 1 7 2.5H5.6V1.8H2.4v.7zM1.6 3h4.8L7 6.5H1z" fill="#1d1d1b"/></svg>012.345.6789</div>Elnombre@website.com<br><strong>www.website.com</strong></div></li>
      <li class="company"><span class="mark" style="font-size:10px">serna interiorisme</span><div class="contact"><strong>El nombre,</strong><div class="phone"><svg width="8" height="7" viewBox="0 0 8 7"><path d="M1 2.5C1 1 2 .5 4 .5S7 1 7 2.5H5.6V1.8H2.4v.7zM1.6 3h4.8L7 6.5H1z" fill="#1d1d1b"/></svg>012.345.6789</div>Elnombre@website.com<br><strong>www.website.com</strong></div></li>
      <li class="company"><span class="mark dark" style="font-size:8.5px">Moret Arquitectos</span><div class="contact"><strong>El nombre,</strong><div class="phone"><svg width="8" height="7" viewBox="0 0 8 7"><path d="M1 2.5C1 1 2 .5 4 .5S7 1 7 2.5H5.6V1.8H2.4v.7zM1.6 3h4.8L7 6.5H1z" fill="#1d1d1b"/></svg>012.345.6789</div>Elnombre@website.com<br><strong>www.website.com</strong></div></li>
      <li class="company"><span class="mark dark" style="font-size:12px">Velara</span><div class="contact"><strong>El nombre,</strong><div class="phone"><svg width="8" height="7" viewBox="0 0 8 7"><path d="M1 2.5C1 1 2 .5 4 .5S7 1 7 2.5H5.6V1.8H2.4v.7zM1.6 3h4.8L7 6.5H1z" fill="#1d1d1b"/></svg>012.345.6789</div>Elnombre@website.com<br><strong>www.website.com</strong></div></li>
    </ul>
    <div class="company-foot"></div>
  </div>

  <div class="panel w1 cover">
    <h1 class="cover-title">POWER<br>TEAM NEXO<br>TARNU</h1>
    <p class="cover-sub">Somos un<br>grupo de empresas</p>
    <div class="cover-band">Grupo de Construcción</div>
    <div class="cover-photo" role="img" aria-label="Fotografía de manos revisando documentos con gráficos sobre una mesa de trabajo"></div>
    <div class="cover-web">www.website.com</div>
    <div style="position:absolute;left:0;right:0;bottom:0;height:17px;background:var(--teal-dark)"></div>
  </div>
</section>

<section class="sheet sheet-inner">
  <div class="panel w1 bg-sky">
    <h2 class="heading" style="margin-top:26px">Diseño y gestión de proyectos y obras para particulares</h2>
    <ul class="services" style="padding-left:25px">
      <li>Proyecto de obra nueva</li>
      <li>Proyecto de reforma y rehabilitación</li>
      <li>Proyecto de interiorismo y decoración</li>
      <li>Proyecto de cambio de uso de locales comerciales y oficinas a vivienda</li>
      <li>Proyecto de legalización de viviendas y otras construcciones</li>
      <li class="muted">Tramitación de licencia de obras ante ayuntamientos y administraciones equivalentes</li>
      <li>Dirección de obra</li>
      <li>Comercialización y valoración de inmuebles, tanto para clientes nacionales como extranjeros que busquen propiedades en España, con especial énfasis en viviendas de alto standing en zonas costeras</li>
    </ul>
    <h2 class="heading" style="margin-top:10px;padding-left:20px">Construcción y obra para particulares</h2>
    <ul class="services" style="padding-left:25px">
      <li>Derribo de construcciones</li>
      <li>Excavación y movimiento de tierras</li>
      <li>Cimentaciones de viviendas</li>
      <li>Estructuras de hormigón, acero y madera para viviendas nuevas</li>
      <li>Refuerzo y reparación de estructuras de hormigón, acero y madera para rehabilitación y/o re-forma de viviendas</li>
      <li>Diseño y construcción de mobiliario a medida</li>
      <li>Diseño y construcción de cocinas a medida de la marca Ribera</li>
      <li>Reforma y rehabilitación de cocinas y baños</li>
      <li>Falsos techos registrables y fijos</li>
      <li>Albañilería tradicional de ladrillo y tabiquería en seco tipo Placor</li>
      <li>Pintura de viviendas y aparcamientos en edificios de viviendas</li>
      <li>Pintura de protección de elementos especiales</li>
      <li>Construcción y reforma de cubiertas, planas o inclinadas, transitables o técnicas, en viviendas y edificios de viviendas</li>
    </ul>
    <div class="inner-strip"></div>
  </div>

  <div class="panel w2 bg-sky">
    <ul class="services" style="padding-top:22px;padding-left:20px">
      <li>Impermeabilización y aislamiento térmico, acústico y estanco en viviendas nuevas y a rehabi-litar o reformar</li>
      <li>Impermeabilización de medianeras mediante tabiques pluviales de diferentes tipos</li>
      <li>Instalación y mantenimiento de calefacción por aire y radiador</li>
      <li>Carpintería de madera en interiores de viviendas</li>
      <li>Instalación y mantenimiento de climatización por aire</li>
      <li>Alicatados en cocinas y baños</li>
      <li>Chapados y revestimientos en viviendas y zonas comunes de edificios de viviendas</li>
      <li>Pavimentos de madera, cerámica y piedra en viviendas y zonas comunes de viviendas</li>
      <li>Carpintería de aluminio en viviendas y edificios de viviendas</li>
      <li>Instalación y mantenimiento de electricidad y domótica</li>
      <li>Instalación y mantenimiento de sistemas de alumbrado, tanto en interiores como en exteriores</li>
      <li>Instalación y mantenimiento de alumbrado de emergencia en zonas comunes de edificios de viviendas</li>
      <li>Instalación y mantenimiento de instalación de fontanería y saneamiento</li>
      <li>Instalación de ascensores especiales para viviendas</li>
      <li>Instalación y mantenimiento de instalaciones de protección contra incendios en aparcamientos de viviendas unifamiliares, aparcamientos de edificios de viviendas y zonas comunes de edificios de viviendas</li>
    </ul>
    <h2 class="heading" style="margin-top:12px;padding-left:12px">Construcción y obra para empresas y negocios</h2>
    <ul class="services" style="padding-left:20px">
      <li>Derribo de construcciones</li>
      <li>Excavación y movimiento de tierras</li>
      <li>Cimentaciones de edificios</li>
      <li>Estructuras de hormigón, acero y madera</li>
      <li>Refuerzo, reparación y modificaciónde estructuras de hormigón, acero y madera para rehabi-litación y/o reforma de edificios</li>
      <li>Diseño y construcción de mobiliario a medida para locales comerciales, oficinas, hoteles y edificios destinados al sector terciario en general</li>
    </ul>
    <div class="inner-strip"></div>
  </div>

  <div class="panel w1 bg-sky">
    <ul class="services" style="padding-top:22px;padding-left:26px">
      <li>Diseño y construcción de cocinas a medida de la marca Ribera</li>
      <li>Reforma y rehabilitación de cocinas y baños en todo tipo de edificios públicos</li>
      <li>Diseño, construcción y mantenimiento de cocinas industriales a medida para hoteles, restau-rantes, cafeterías, escuelas, hospitales y cualquier establecimiento público que necesite este tipo de servicio, completamente equipada con la maquinaria más adecuada a sus requerimien-tos</li>
      <li>Pintura de protección de elementos especiales</li>
      <li>Construcción y reforma de cubiertas, tanto transitables como técnicas</li>
      <li>Asesoramiento sobre las mejores soluciones de eficiencia energética en el equipamiento de locales comerciales, hoteles y toda clase de edificios públicos que precisen de una mejora en su consumo de energía</li>
      <li>Albañilería tradicional de ladrillo y tabiquería en seco tipo Placor, ya sea estándar o con re-querimientos acústicos y/o de protección al fuego especiales</li>
      <li>Pintura de viviendas y aparcamientos, aplicando en cada caso el producto más adecuado a las necesidades y las exigencias de su uso</li>
      <li>Falsos techos registrables y fijos</li>
      <li>Alicatados en cocinas y baños</li>
      <li>Impermeabilización y aislamiento térmico, acústico y estanco</li>
      <li>Impermeabilización de elementos especiales de exterior, en especial paredes medianeras</li>
      <li>Instalación y mantenimiento de climatización. Además de los métodos tradicionales, como la climatización por aire, por radiadores o convectores, somo expertos en aerotermia, geotermia y energía solar, así como el tratamiento del aire en entornos que requieran de una calidad es-pecial en este aspecto</li>
      <li>Chapados y revestimientos de paredes y fachadas</li>
      <li>Pavimentos de madera, cerámica y piedra, así como pavimentos técnicos</li>
      <li>Carpintería de madera en interiores</li>
      <li>Recuperación de elementos interiores de madera</li>
      <li>Carpintería de aluminio</li>
    </ul>
    <div class="inner-strip"></div>
  </div>
</section>

<div class="side-label" style="left:36px;top:1140px">Side 2</div>
<div class="side-label" style="left:262px;top:1140px">Side 3</div>
<div class="side-label" style="left:482px;top:1140px">Side 4</div>
</body>
</html>
```